Small Accounting Practice needs something creative

We need a business card design for a new small accounting practice based in Perth, Australia. The name of the practice is 'Kelvarin Ledger Group Pty Ltd'. We providing Tax, Bookkeeping and Accounting services. Our target are individuals and small businesses. We want the design to be simply and creative. Also, we can the design can help us to gain people's trust.

Target Market(s)

Individuals and small businesses.

Industry/Entity Type

Accounting

Colors

Designer to choose colors to be used in the design.

```html
<!DOCTYPE html>
<html lang="en">
<head>
<meta charset="utf-8">
<title>Kelvarin Ledger Group – Business Card</title>
<link rel="stylesheet" href="https://fonts.googleapis.com/css2?family=Nunito:wght@800&family=Open+Sans:wght@400;600&display=swap">
<style>
  :root {
    --backdrop: #1e1e1e;
    --card-white: #ffffff;
    --card-dark: #1a1a1a;
    --card-dark-2: #2a2a2a;
    --brand-teal: #2e87a5;
    --ink: #1c1c1c;
    --muted: #d8d8d8;
    --puzzle-grey: #8a8a8a;
    --puzzle-light: #ececec;
  }
  * { margin: 0; padding: 0; box-sizing: border-box; }
  html, body { width: 1200px; height: 800px; overflow: hidden; }
  body {
    background: var(--backdrop);
    font-family: "Open Sans", Arial, sans-serif;
    position: relative;
  }
  .card {
    position: absolute;
    top: 245px;
    width: 525px;
    height: 310px;
    box-shadow: 0 10px 30px rgba(0,0,0,.55);
    overflow: hidden;
  }
  /* Front */
  .card--front { left: 45px; background: var(--card-white); }
  .front__band {
    position: absolute; left: 0; right: 0; bottom: 0; height: 52px;
    background: repeating-linear-gradient(45deg, var(--card-dark) 0 3px, var(--card-dark-2) 3px 6px);
    border-top: 7px solid var(--brand-teal);
  }
  .front__agent {
    position: absolute; left: 22px; bottom: 12px;
    font-size: 9px; color: var(--muted); letter-spacing: .3px;
  }
  .front__art {
    position: absolute; left: 30px; top: 26px; width: 150px; height: 120px;
    border-radius: 8px;
    background: linear-gradient(135deg, var(--puzzle-grey) 0%, var(--puzzle-light) 70%);
  }
  .brand {
    display: flex; align-items: center; gap: 10px;
  }
  .brand__dot {
    width: 28px; height: 28px; border-radius: 50%;
    background: var(--brand-teal); flex: none;
  }
  .brand__name {
    font-family: "Nunito", Arial, sans-serif; font-weight: 800;
    color: var(--brand-teal); line-height: 1.05;
  }
  .front__brand { position: absolute; left: 215px; top: 40px; }
  .front__brand .brand__name { font-size: 22px; width: 260px; }
  .person { position: absolute; left: 215px; top: 112px; }
  .person__name {
    font-family: "Nunito", Arial, sans-serif; font-weight: 800;
    font-size: 27px; color: var(--brand-teal); line-height: 1.1;
  }
  .person__role { font-size: 11px; font-weight: 600; color: var(--ink); margin-top: 2px; }
  .contacts { list-style: none; margin-top: 10px; }
  .contacts li {
    display: flex; align-items: center; gap: 8px;
    font-size: 11.5px; color: var(--ink); height: 19px;
  }
  .contacts li.phone { font-size: 14px; }
  .icon { width: 14px; height: 14px; flex: none; }
  .icon--square { background: var(--brand-teal); border-radius: 2px; }
  /* Back */
  .card--back {
    left: 630px;
    background: repeating-linear-gradient(45deg, var(--card-dark) 0 3px, var(--card-dark-2) 3px 6px);
    display: flex; align-items: center; justify-content: center;
  }
  .back__badge {
    width: 420px; height: 250px; border-radius: 50%;
    background: radial-gradient(ellipse at center, #ffffff 60%, #e6e6e6 100%);
    border: 8px solid #bdbdbd;
    display: flex; align-items: center; justify-content: center;
  }
  .back__badge .brand__dot { width: 38px; height: 38px; }
  .back__badge .brand__name { font-size: 28px; width: 250px; }
</style>
</head>
<body>

<section class="card card--front" aria-label="Business card front">
  <div class="front__art" role="img" aria-label="Two interlocking puzzle pieces, grey and white"></div>

  <div class="brand front__brand">
    <span class="brand__dot"></span>
    <span class="brand__name">Kelvarin Ledger Group Pty Ltd</span>
  </div>

  <div class="person">
    <h1 class="person__name">Tomas Reyna</h1>
    <p class="person__role">Accountant &amp; Small Business Consultant</p>
    <ul class="contacts">
      <li class="phone">
        <svg class="icon" viewBox="0 0 16 16"><path d="M4 1h3l1 4-2 1a9 9 0 0 0 4 4l1-2 4 1v3a2 2 0 0 1-2 2A13 13 0 0 1 2 3a2 2 0 0 1 2-2z" fill="#1c1c1c"/></svg>
        000-000-0000
      </li>
      <li>
        <svg class="icon" viewBox="0 0 16 16"><rect x="1" y="3" width="14" height="10" rx="1" fill="#2e87a5"/><path d="M1.5 4 8 9l6.5-5" stroke="#fff" stroke-width="1.3" fill="none"/></svg>
        tomas@kelvarinledger.com.au
      </li>
      <li><span class="icon icon--square"></span>Profile</li>
    </ul>
  </div>

  <div class="front__band">
    <span class="front__agent">Registered ASIC Agent 48067</span>
  </div>
</section>

<section class="card card--back" aria-label="Business card back">
  <div class="back__badge">
    <div class="brand">
      <span class="brand__dot"></span>
      <span class="brand__name">Kelvarin Ledger Group Pty Ltd</span>
    </div>
  </div>
</section>

</body>
</html>
```